Postcard Design

I have an accounting firm and I would like to increase my customer base by a postcard mailout/letter dropI want a design that is eye catching and uses my logo. I specialise in small to medium business and offer services for commercial accounting and business advisory. I also want to offer a discount for new clients.Previously I had my website updated and would like to stay with the theme

Industry/Entity Type

Business Consultant

Font styles to use
Serif

Colors
b667aa
d3a5cc

Requirements
Must have
• the post card needs to be arty to attract attention. also business like

```html
<!DOCTYPE html>
<html lang="en">
<head>
<meta charset="utf-8">
<title>Lorimer Accounting Services – Postcard</title>
<link rel="stylesheet" href="https://fonts.googleapis.com/css2?family=Alegreya+Sans+SC:wght@400&family=Cabin:ital,wght@0,400;0,600;1,600&family=Handlee&display=swap">
<style>
  :root{
    --purple:#b667aa;
    --purple-deep:#9c3f92;
    --purple-text:#8a1f86;
    --lilac:#d3a5cc;
    --grey-text:#555a60;
    --paper:#ffffff;
    --photo-light:#e6edf5;
    --photo-mid:#b6c6d8;
    --photo-dark:#5d6c80;
    --tag-red:#e3262b;
    --tag-green:#8ccf2a;
    --tag-violet:#7b44b0;
  }
  *{margin:0;padding:0;box-sizing:border-box}
  html,body{width:776px;height:1200px;overflow:hidden;background:var(--paper)}
  .canvas{position:relative;width:776px;height:1200px}
  .card{position:absolute;left:26px;background:var(--paper);overflow:hidden;box-shadow:0 0 6px rgba(0,0,0,.18)}
  .card--front{top:27px;width:720px;height:567px}
  .card--back{top:614px;width:722px;height:559px}
  .card__art{position:absolute;inset:0}
  .brand-name{position:absolute;font-family:"Alegreya Sans SC",sans-serif;font-weight:400;letter-spacing:.5px;white-space:nowrap}
  .front__name{left:172px;top:404px;font-size:38px;color:var(--grey-text)}
  .front__tagline{position:absolute;left:172px;top:454px;font-family:"Handlee",cursive;font-size:20px;color:var(--purple-deep);letter-spacing:.3px}
  .phone{position:absolute;display:flex;align-items:center;gap:6px;font-family:"Cabin",sans-serif;white-space:nowrap}
  .front__phone{left:176px;top:493px;font-size:26px;color:var(--grey-text)}
  .front__web{position:absolute;left:392px;top:504px;font-family:"Cabin",sans-serif;font-size:11.5px;letter-spacing:.6px;color:var(--grey-text);display:flex;align-items:center;gap:8px}
  .back__name{left:119px;top:28px;font-size:29px;color:#fff}
  .back__phone{left:122px;top:67px;font-size:22px;color:#fff}
  .back__address{position:absolute;left:392px;top:85px;font-family:"Cabin",sans-serif;font-style:normal;font-size:12.5px;line-height:19px;color:#333}
  .back__copy{position:absolute;left:23px;top:158px;width:340px;font-family:"Cabin",sans-serif;color:var(--purple-text)}
  .intro{font-style:italic;font-weight:600;font-size:14px;line-height:20px;margin-bottom:2px}
  .section-title{font-weight:600;font-size:14px;text-decoration:underline;line-height:20px}
  .list{list-style:none;font-weight:600;font-size:14px;line-height:20px;width:338px}
  .list li{position:relative;padding-left:33px;padding-right:26px}
  .list li::before{content:"";position:absolute;left:4px;top:8px;width:4px;height:4px;border-radius:50%;background:var(--purple-text)}
  .tag{position:absolute;font-family:"Cabin",sans-serif;font-weight:600;color:#fff;text-align:center;line-height:1.1;display:flex;flex-direction:column;justify-content:center;box-shadow:3px 4px 6px rgba(0,0,0,.3);transform:rotate(-12deg)}
  .tag__head{text-decoration:underline;font-size:13px}
  .tag__sub{font-size:13px}
  .tag--advice{left:24px;top:472px;width:128px;height:70px;background:var(--tag-red)}
  .tag--advice .tag__head,.tag--advice .tag__sub{font-size:15px}
  .tag--experts{left:140px;top:458px;width:118px;height:64px;background:var(--tag-green)}
  .tag--strategies{left:240px;top:446px;width:108px;height:56px;background:var(--tag-violet)}
</style>
</head>
<body>
<main class="canvas">

  <section class="card card--front" aria-label="Postcard front">
    <svg class="card__art" width="720" height="567" viewBox="0 0 720 567">
      <defs>
        <linearGradient id="front-photo" x1="0" y1="0" x2="1" y2="1">
          <stop offset="0" stop-color="var(--photo-dark)"/>
          <stop offset=".35" stop-color="var(--photo-mid)"/>
          <stop offset="1" stop-color="var(--photo-light)"/>
        </linearGradient>
        <linearGradient id="front-band" x1="0" y1="0" x2="1" y2="0">
          <stop offset="0" stop-color="#b04fa6"/>
          <stop offset="1" stop-color="#c873bc"/>
        </linearGradient>
      </defs>
      <path role="img" aria-label="Photo of a calculator and pen resting on a statement of cash flows" d="M0,0 H720 V335 C480,290 240,310 0,290 Z" fill="url(#front-photo)"/>
      <path d="M0,290 C240,310 480,290 720,335 V357 C560,395 380,405 0,381 Z" fill="url(#front-band)"/>
      <circle cx="90" cy="446" r="52" fill="var(--lilac)"/>
    </svg>
    <div class="brand-name front__name">Lorimer Accounting Services</div>
    <div class="front__tagline">The Accountants with Professional Integrity</div>
    <div class="phone front__phone">
      <svg width="24" height="24" viewBox="0 0 24 24" aria-hidden="true"><circle cx="12" cy="12" r="10.5" fill="none" stroke="currentColor" stroke-width="1.8"/><path d="M8 16c2-4 4-6 8-8" stroke="currentColor" stroke-width="2.4" stroke-linecap="round" fill="none"/></svg>
      02 4911 2730
    </div>
    <div class="front__web">
      <svg width="12" height="12" viewBox="0 0 12 12" aria-hidden="true"><circle cx="6" cy="6" r="5.2" fill="none" stroke="currentColor"/><path d="M6 5v4M6 3v.8" stroke="currentColor" stroke-width="1.2"/></svg>
      WWW.LORIMERACCOUNTINGSERVICES.COM
    </div>
  </section>

  <section class="card card--back" aria-label="Postcard back">
    <svg class="card__art" width="722" height="559" viewBox="0 0 722 559">
      <defs>
        <linearGradient id="back-photo" x1="0" y1="0" x2="1" y2="1">
          <stop offset="0" stop-color="#eef2f7"/>
          <stop offset=".6" stop-color="#dde5ee"/>
          <stop offset="1" stop-color="#f4f6f9"/>
        </linearGradient>
        <linearGradient id="back-band" x1="0" y1="0" x2="1" y2="0">
          <stop offset="0" stop-color="#b552aa"/>
          <stop offset="1" stop-color="#c15fb5"/>
        </linearGradient>
      </defs>
      <rect role="img" aria-label="Faded photo of hands working a calculator over financial papers" x="0" y="90" width="370" height="410" fill="url(#back-photo)"/>
      <path d="M0,0 H722 V122 C660,100 600,78 520,74 C420,70 330,95 230,120 C150,140 80,152 0,151 Z" fill="url(#back-band)"/>
      <circle cx="65" cy="65" r="40" fill="var(--lilac)"/>
      <rect x="600" y="38" width="94" height="113" fill="#fff" stroke="#4a2c70" stroke-width="2" stroke-dasharray="7 5"/>
      <g stroke="#4a2c70" stroke-width="1.6" stroke-dasharray="8 6">
        <line x1="388" y1="295" x2="705" y2="295"/>
        <line x1="388" y1="364" x2="705" y2="364"/>
        <line x1="388" y1="433" x2="705" y2="433"/>
      </g>
    </svg>
    <div class="brand-name back__name">Lorimer Accounting Services</div>
    <div class="phone back__phone">
      <svg width="20" height="20" viewBox="0 0 24 24" aria-hidden="true"><circle cx="12" cy="12" r="10.5" fill="none" stroke="currentColor" stroke-width="1.8"/><path d="M8 16c2-4 4-6 8-8" stroke="currentColor" stroke-width="2.4" stroke-linecap="round" fill="none"/></svg>
      02 4911 2730
    </div>
    <address class="back__address">
      Level 2, 48 Harbour Lane ,<br>Newcastle NSW<br>Australia 2300
    </address>
    <div class="back__copy">
      <p class="intro">As Business Advisory and Commercial Accountant<br>we welcome the opportunity to earn your trust<br>and deliver the best service in the industry.</p>
      <h2 class="section-title">WE SERVE</h2>
      <ul class="list">
        <li>Mid North Coast of New South Wales</li>
        <li>Sydney CBD</li>
        <li>The Newcastle Hunter Region</li>
      </ul>
      <h2 class="section-title">OUR BENEFITS</h2>
      <ul class="list">
        <li>We are Committed to Innovative Accounting<br>Strategies</li>
        <li>We are Professionally Qualified Accountants</li>
        <li>We Proactively Deliver Services</li>
        <li>We Support Our Clients in Achieving<br>Business Goals</li>
      </ul>
    </div>
    <div class="tag tag--advice"><span class="tag__head">ADVICE</span><span class="tag__sub">You can<br>rely on</span></div>
    <div class="tag tag--experts"><span class="tag__head">EXPERTS</span><span class="tag__sub">Who've<br>been there</span></div>
    <div class="tag tag--strategies"><span class="tag__head">STRATEGIES</span><span class="tag__sub">That work</span></div>
  </section>

</main>
</body>
</html>
```